Funky Modern Flyer A5 or Postcard size

Hi, I am looking at a one small flyer (A5 or postcard size) that I can put both on my website on the front page (ie so png) and also send out if necessary.

It has to be modern, funky and hip. My brand is professional / Corporate so it also has to fit in with that brand.

There are 6 attachments:
Example 1 - Kavorra - I like this look, clean, modern, funky and says it all.
Example 2 - Kavora - again another look I like, simple, explanatory
Example 4 - Artisan Bazaar - font is cool on this one but background not so much too much going on but I like the font
Example 5 - Example 4 - Artisan Bazaar - font is cool on this one but background not so much too much going on but I like the font
5 is my logo
Example 6 is something I found on the web this morning which is effective.

It is for a Mentoring and Training program I run called: SKYWARD

What is to be included is the following:
The name: Skyward
Somewhere: Training, Mentoring
My Logo (see attached two options) you can choose which colour suits and I have the source file should you need it
My website and email: www.deliamarsk.example / delia@deliamarsk.example

This wording: This is one of our highest in-demand programs and is based on a background and proven track record by Delia in accelerating sales organisations and their people into stand out high performers. **(NOTE this wording in this paragraph may change and I am open to you changing if you think you can make it more effective!)

Colours: white, black and gold (those are our website colours).

I'd like the Skyward to really stand out.... I have included two fonts that I really like that I got off Artisan Bazaar. However, feel free to suggest other fonts that you think cool or funky!
Updates

Hi everyone, just to add a note to the brief, I am not overly keen on pictures that are really busy. I only like a picture that is minimal and effective. The examples from Artisan Bazaar was more for the Font Style not so much the pictures in the background. The pictures can take away from a design unless done really minimally.....hope this makes sense. Delia Added Wednesday, March 15, 2017

Target Market(s)

My target Market is Corporates but I want a Funky Modern look as a lot of people in Corporates are Millennials as well which is part of my target market

Industry/Entity Type

Information Technology

Requirements
Must have
• What is to be included is the following:
• The name: Skyward
• Somewhere: Training, Mentoring
• My Logo (see attached two options) you can choose which colour suits and I have the source file should you need it
• My website and email: www.deliamarsk.example / delia@deliamarsk.example
• This wording: This is one of our highest in-demand programs and is based on a background and proven track record in high performance and accelerating sales organisations and their people into stand out high performers. (**NOTE this wording may change when final design is picked to be changed as still working in it***)
• Colours: white, black and gold (those are our website colours).
• I'd like the Skyward to really stand out.... I have included two fonts that I really like that I got off Artisan Bazaar. However, feel free to suggest other fonts that you think cool or funky! NOTE: The pictures I have attached is mainly for the FONTS not for the background pictures. I am not that keen on background pictures as it can take away from the font - unless it is minimal
Should not have
• Too many different colours, I like slick, modern, clean. White, gold and black preferred as this is our website colour.
• NOTE: The pictures from Artisan Bazaar I have attached are mainly for the FONTS not for the background pictures. I am not hugely keen on background pictures as it can take away from the font/message - unless the pictures are minimal but effective.

```html
<!DOCTYPE html>
<html lang="en">
<head>
<meta charset="utf-8">
<title>Skyward – Training, Mentoring Flyer</title>
<link rel="stylesheet" href="https://fonts.googleapis.com/css2?family=Kaushan+Script&family=Open+Sans:wght@300;400;700&display=swap">
<style>
  :root {
    --black: #0a0a0a;
    --gold: #f0b323;
    --gold-light: #f7d35e;
    --white: #ffffff;
    --paper: #f3f3f3;
    --ink: #1c1c1c;
    --grey: #555555;
    --stage: #d9d9d9;
  }
  * { margin: 0; padding: 0; box-sizing: border-box; }
  html, body {
    width: 1200px; height: 1200px; overflow: hidden;
    background: var(--stage);
  }
  .flyer {
    position: absolute; left: 192px; top: 50px;
    width: 725px; height: 978px;
    transform: scale(1.125); transform-origin: 0 0;
    background: var(--paper);
    overflow: hidden;
    font-family: "Open Sans", Arial, sans-serif;
    box-shadow: 0 6px 18px rgba(0,0,0,.25);
  }
  .flyer__shapes { position: absolute; inset: 0; width: 725px; height: 978px; }
  .title {
    position: absolute; left: 0; right: 0; top: 96px;
    text-align: center;
    font-family: "Kaushan Script", cursive;
    font-size: 100px; line-height: 1;
    color: var(--white);
  }
  .brand-mark {
    position: absolute; left: 138px; top: 468px;
    font-size: 56px; font-weight: 300; letter-spacing: 2px;
    color: var(--grey);
  }
  .brand-name {
    position: absolute; left: 58px; top: 560px;
    font-size: 29px; font-weight: 300; letter-spacing: 2px;
    color: var(--grey);
  }
  .services {
    position: absolute; left: 36px; top: 608px;
    font-size: 38px; font-weight: 700; letter-spacing: .3px;
    color: var(--gold);
  }
  .pitch {
    position: absolute; left: 36px; top: 665px; width: 585px;
    font-size: 16.5px; line-height: 22px;
    text-align: justify; color: var(--ink);
  }
  .portrait {
    position: absolute; left: 45px; top: 742px;
    width: 200px; height: 200px; border-radius: 50%;
    border: 3px solid var(--black);
    background: radial-gradient(circle at 50% 40%, #dcdcdc 0%, #9a9a9a 55%, #3a3a3a 100%);
  }
  .phone {
    position: absolute; left: 320px; top: 822px;
    display: flex; align-items: center; gap: 34px;
    font-size: 36px; color: var(--ink);
  }
  .contacts {
    position: absolute; left: 256px; top: 892px;
    display: flex; gap: 12px; align-items: center;
    font-size: 15px; color: var(--ink);
  }
  .contact { display: flex; align-items: center; gap: 6px; }
</style>
</head>
<body>
  <main class="flyer">
    <svg class="flyer__shapes" viewBox="0 0 725 978">
      <defs>
        <linearGradient id="photoTone" x1="0" y1="0" x2="1" y2="1">
          <stop offset="0" stop-color="#f4f1ec"/>
          <stop offset="0.6" stop-color="#e8d3be"/>
          <stop offset="1" stop-color="#d8a784"/>
        </linearGradient>
        <linearGradient id="bandFade" x1="0" y1="0" x2="1" y2="0">
          <stop offset="0" stop-color="#f0b323"/>
          <stop offset="0.55" stop-color="#f3c03c"/>
          <stop offset="1" stop-color="#f8dc86"/>
        </linearGradient>
        <linearGradient id="bandFadeLight" x1="0" y1="0" x2="1" y2="0">
          <stop offset="0" stop-color="#f7d35e"/>
          <stop offset="1" stop-color="#fbe9b0"/>
        </linearGradient>
      </defs>
      <polygon class="photo" role="img" aria-label="Photograph of a hand pointing at a pie chart on a printed report"
               points="355,377 725,227 725,560 430,460" fill="url(#photoTone)"/>
      <polygon class="header" points="0,0 725,0 725,227 355,377 0,222" fill="var(--black)"/>
      <polygon class="band band--gold" points="0,222 725,532 725,600 0,291" fill="url(#bandFade)"/>
      <polygon class="band band--light" points="0,291 725,600 725,667 0,360" fill="url(#bandFadeLight)"/>
      <rect class="footer-bar" x="0" y="950" width="725" height="28" fill="var(--black)"/>
      <polygon class="footer-accent" points="580,950 725,950 725,978 570,978" fill="var(--gold)"/>
    </svg>

    <h1 class="title">Skyward</h1>
    <div class="brand-mark">DM</div>
    <div class="brand-name">DELIA MARSK</div>
    <h2 class="services">TRAINING, MENTORING</h2>
    <p class="pitch">This is one of our highest in-demand programs and is based on a background and proven track record in high performance and accelerating sales organisations and their people into stand out high performers</p>

    <div class="portrait" role="img" aria-label="Black and white portrait photo of Delia Marsk"></div>

    <div class="phone">
      <svg width="46" height="40" viewBox="0 0 46 40" aria-hidden="true">
        <path d="M3 14 C3 4 43 4 43 14 L35 16 L33 11 C27 9 19 9 13 11 L11 16 Z" fill="var(--gold)"/>
        <path d="M12 18 L34 18 L40 38 L6 38 Z" fill="var(--gold)"/>
        <circle cx="23" cy="28" r="6" fill="var(--white)"/>
        <circle cx="23" cy="28" r="3" fill="var(--gold)"/>
      </svg>
      <span>6420555017</span>
    </div>

    <div class="contacts">
      <span class="contact">
        <svg width="20" height="16" viewBox="0 0 20 16" aria-hidden="true">
          <rect x="1" y="2" width="18" height="12" fill="none" stroke="var(--gold)" stroke-width="1.5"/>
          <path d="M1 2 L10 9 L19 2" fill="none" stroke="var(--gold)" stroke-width="1.5"/>
        </svg>
        delia@deliamarsk.example
      </span>
      <span class="contact">
        <svg width="22" height="18" viewBox="0 0 22 18" aria-hidden="true">
          <rect x="1" y="1" width="20" height="12" fill="none" stroke="var(--gold)" stroke-width="1.5"/>
          <path d="M8 17 L14 17 M11 13 L11 17" stroke="var(--gold)" stroke-width="1.5"/>
        </svg>
        www.deliamarsk.example
      </span>
    </div>
  </main>
</body>
</html>
```